IT Service Provider

We need a website which reflects the IT Services we can offer to small and mid-size companies. This reaches from LAN/WAN, Security, VoIP, WiFi, Storage, Penetration testing.and Support.

In addition to that, a Logo is needed and should be embedded in the website.

Company is registered in the UK under:
Pellwick Ltd
Company No. 05927318

Industry/Entity Type

Security

```html
<!DOCTYPE html>
<html lang="en">
<head>
<meta charset="utf-8">
<title>Pellwick – IT Services</title>
<link href="https://fonts.googleapis.com/css2?family=Mulish:wght@400;600;700&display=swap" rel="stylesheet">
<style>
:root{
  --teal:#0f9a80;
  --blue:#1c6a96;
  --navy:#14628f;
  --text:#4a4a4a;
  --dark:#3a3a3a;
  --light:#f1f1f1;
  --white:#ffffff;
  --muted:#cfcfcf;
}
*{box-sizing:border-box;margin:0;padding:0}
html,body{width:1200px;height:2296px;overflow:hidden}
body{font-family:"Mulish",Arial,sans-serif;color:var(--text);background:var(--white);position:relative}
a{text-decoration:none;color:inherit}
section,header,footer{position:absolute;left:0;width:1200px}
.section-title{position:absolute;left:0;width:1200px;text-align:center;font-size:22px;font-weight:400;color:var(--teal);letter-spacing:.5px}
.btn{position:absolute;display:flex;align-items:center;justify-content:center;background:var(--navy);color:var(--white);font-size:12px;letter-spacing:.4px}

/* header */
.site-header{top:0;height:92px}
.brand{position:absolute;left:73px;top:26px;display:flex;align-items:center;gap:10px;font-size:30px;font-weight:700;color:var(--teal)}
.brand-mark{width:40px;height:40px;border:3px solid var(--teal);border-radius:6px}
.main-nav{position:absolute;right:73px;top:38px;display:flex;gap:54px;font-size:13px;color:#333}

/* hero */
.hero{top:92px;height:443px;background:linear-gradient(90deg,#b8c3d3 0%,#c7d4e6 40%,#b6c7e0 100%)}
.hero-visual{position:absolute;left:0;top:0;width:720px;height:443px;background:linear-gradient(90deg,rgba(150,160,175,.55),rgba(190,205,225,0))}
.hero-headline{position:absolute;right:73px;top:122px;text-align:right;font-size:30px;line-height:38px;font-weight:600;color:var(--blue)}
.hero .btn{left:975px;top:260px;width:152px;height:42px;background:var(--teal);font-size:15px;font-weight:600}
.slider-dots{position:absolute;left:568px;top:416px;display:flex;gap:6px}
.slider-dots span{width:11px;height:11px;border-radius:50%;background:#3b4656}
.slider-dots span:first-child{background:var(--teal)}

/* welcome */
.welcome{top:535px;height:268px}
.welcome .section-title{top:42px}
.welcome p{position:absolute;left:73px;width:1054px;top:86px;text-align:center;font-size:12.3px;line-height:26.5px}
.welcome .btn{left:530px;top:185px;width:139px;height:42px}

/* services */
.services{top:803px;height:330px;background:var(--teal)}
.services .section-title{top:34px;color:var(--white)}
.service{position:absolute;top:91px;width:180px;margin-left:-90px;text-align:center}
.service-icon{width:125px;height:125px;border-radius:50%;background:var(--white);margin:0 auto;display:flex;align-items:center;justify-content:center}
.service h3{margin-top:20px;font-size:19px;font-weight:600;color:var(--white);letter-spacing:.4px}
.service a{display:block;margin-top:14px;font-size:11px;color:#1f3c3a}

/* news */
.news{top:1133px;height:346px}
.news .section-title{top:36px}
.news-item{position:absolute;top:92px;width:320px}
.news-item time{display:block;font-size:13px;font-weight:700;color:var(--blue)}
.news-item p{margin-top:6px;font-size:11.8px;line-height:21px}
.news-item a{display:block;margin-top:6px;font-size:12px;color:var(--teal)}
.news-divider{position:absolute;top:95px;width:1px;height:130px;background:#e3e3e3}
.news .btn{left:530px;top:265px;width:139px;height:42px}

/* clients */
.clients{top:1479px;height:181px;background:var(--light)}
.clients .section-title{top:30px}
.client-row{position:absolute;top:95px;left:0;width:1200px;display:flex;justify-content:center;gap:34px;font-size:17px;font-weight:700;color:#555}

/* team */
.team{top:1660px;height:273px}
.team .section-title{top:41px}
.member{position:absolute;top:117px;width:510px}
.member-photo{position:absolute;left:0;top:0;width:90px;height:90px;border-radius:50%;background:linear-gradient(135deg,#b58d76,#6d5a52)}
.member-body{position:absolute;left:116px;top:-2px;width:400px}
.member-body h4{font-size:13px;font-weight:600;color:var(--blue)}
.member-body p{margin-top:4px;font-size:11.8px;line-height:21px}
.member-body a{display:block;margin-top:6px;font-size:12px;color:var(--blue)}

/* footer */
.site-footer{top:1933px;height:363px;background:var(--dark);color:var(--white)}
.site-footer .section-title{top:47px;color:var(--white)}
.footer-col{position:absolute;top:100px}
.footer-col h5{font-size:13px;font-weight:400;letter-spacing:.3px}
.address{margin-top:12px;font-size:11px;line-height:20px;color:#e8e8e8}
.address strong{font-weight:600}
.map{position:absolute;left:306px;top:129px;width:542px;height:208px;background:linear-gradient(135deg,#dfe4d6,#cfd9c4 55%,#e3e1d8)}
.map-popup{position:absolute;left:160px;top:26px;width:258px;padding:6px 8px;background:var(--white);color:#333;font-size:10.5px;line-height:14px;text-align:center;box-shadow:0 1px 3px rgba(0,0,0,.3)}
.map-pin{position:absolute;left:282px;top:128px}
.social{display:flex;gap:7px;margin-top:14px}
.social span{width:30px;height:30px;border-radius:50%;background:var(--teal)}
.footer-brand{position:absolute;left:884px;top:250px;display:flex;align-items:center;gap:8px;font-size:25px;font-weight:600;color:#bdbdbd}
.footer-brand .brand-mark{width:32px;height:32px;border-color:#bdbdbd}
.legal{position:absolute;left:884px;top:305px;font-size:11px;line-height:18px;color:var(--muted)}
</style>
</head>
<body>

<header class="site-header">
  <a class="brand" href="#"><span class="brand-mark"></span>Pellwick</a>
  <nav class="main-nav">
    <a href="#">Home</a><a href="#">About Us</a><a href="#">Services</a><a href="#">Latest News</a><a href="#">Blog</a><a href="#">Clients</a><a href="#">Contact</a>
  </nav>
</header>

<section class="hero">
  <div class="hero-visual" role="img" aria-label="Businessman in a grey suit touching a cloud network diagram above a laptop"></div>
  <h1 class="hero-headline">We provide LAN/WAN, Security,<br>VoIP, WiFi, Storage, Penetration<br>testing.and Support.</h1>
  <a class="btn" href="#">READ MORE ››</a>
  <div class="slider-dots"><span></span><span></span><span></span><span></span></div>
</section>

<section class="welcome">
  <h2 class="section-title">WELCOME TO OUR WEBSITE</h2>
  <p>Aliquam molestie, mi et imperdiet euismod, dui purus auctor tellus, et interdum lacus lectus et ante. Sed accumsan sollicitudin sapien, sit amet adipiscing turpis gravida ac. In congue, neque ac lobortis volutpat, libero mauris varius mi, vitae suscipit ipsum ligula vitae risus. Duis aliquam nibh a dui iaculis viverra id a velit. Vivamus egestas risus in magna varius commodo. Sed semper viverra egestas. Etiam pretium porttitor lectus, vel ornare neque porta volutpat.</p>
  <a class="btn" href="#">READ MORE ››</a>
</section>

<section class="services">
  <h2 class="section-title">WHAT WE DO</h2>
  <div class="service" style="left:151px">
    <div class="service-icon"><svg width="60" height="56" viewBox="0 0 60 56" fill="#1c6a96"><rect x="22" y="0" width="16" height="13"/><rect x="0" y="40" width="16" height="13"/><rect x="22" y="40" width="16" height="13"/><rect x="44" y="40" width="16" height="13"/><rect x="28" y="13" width="4" height="27"/><rect x="6" y="25" width="48" height="4"/><rect x="6" y="25" width="4" height="15"/><rect x="50" y="25" width="4" height="15"/></svg></div>
    <h3>LAN/WAN</h3><a href="#">Learn More ››</a>
  </div>
  <div class="service" style="left:331px">
    <div class="service-icon"><svg width="58" height="58" viewBox="0 0 58 58" fill="none" stroke="#1c6a96" stroke-width="4"><circle cx="10" cy="10" r="7" fill="#1c6a96"/><circle cx="46" cy="10" r="7" fill="#1c6a96"/><circle cx="10" cy="46" r="7" fill="#1c6a96"/><path d="M17 10h22M10 17v22M15 15l14 14"/><rect x="30" y="36" width="22" height="18" fill="#1c6a96" stroke="none"/><path d="M34 36v-5a7 7 0 0 1 14 0v5"/></svg></div>
    <h3>SECURITY</h3><a href="#">Learn More ››</a>
  </div>
  <div class="service" style="left:511px">
    <div class="service-icon"><svg width="64" height="50" viewBox="0 0 64 50" fill="#1c6a96"><path d="M4 16C4 6 60 6 60 16v6H44v-6H20v6H4z"/><path d="M12 24h40l8 24H4z"/><g fill="#fff"><rect x="18" y="30" width="6" height="4"/><rect x="29" y="30" width="6" height="4"/><rect x="40" y="30" width="6" height="4"/><rect x="16" y="38" width="6" height="4"/><rect x="29" y="38" width="6" height="4"/><rect x="42" y="38" width="6" height="4"/></g></svg></div>
    <h3>VOIP</h3><a href="#">Learn More ››</a>
  </div>
  <div class="service" style="left:690px">
    <div class="service-icon"><svg width="64" height="52" viewBox="0 0 64 52" fill="none" stroke="#1c6a96" stroke-width="6" stroke-linecap="round"><path d="M5 18a38 38 0 0 1 54 0"/><path d="M14 28a25 25 0 0 1 36 0"/><path d="M23 38a12 12 0 0 1 18 0"/><circle cx="32" cy="47" r="2" fill="#1c6a96"/></svg></div>
    <h3>WiFi</h3><a href="#">Learn More ››</a>
  </div>
  <div class="service" style="left:870px">
    <div class="service-icon"><svg width="62" height="54" viewBox="0 0 62 54" fill="#1c6a96"><path d="M18 24a10 10 0 0 1 10-14 13 13 0 0 1 24 6 8 8 0 0 1 0 12H20a7 7 0 0 1-2-4z"/><path d="M6 34h50l4 8v10H2V42z"/><rect x="8" y="44" width="28" height="3" fill="#fff"/><circle cx="50" cy="46" r="2.5" fill="#fff"/></svg></div>
    <h3>STORAGE</h3><a href="#">Learn More ››</a>
  </div>
  <div class="service" style="left:1050px">
    <div class="service-icon"><svg width="56" height="58" viewBox="0 0 56 58"><circle cx="28" cy="22" r="13" fill="#1c6a96"/><path d="M8 58c0-14 9-20 20-20s20 6 20 20z" fill="#1c6a96"/><path d="M11 24a17 17 0 0 1 34 0" fill="none" stroke="#1c6a96" stroke-width="4"/><rect x="7" y="20" width="7" height="12" rx="3" fill="#1c6a96"/><rect x="42" y="20" width="7" height="12" rx="3" fill="#1c6a96"/></svg></div>
    <h3>SUPPORT</h3><a href="#">Learn More ››</a>
  </div>
</section>

<section class="news">
  <h2 class="section-title">LATEST NEWS</h2>
  <article class="news-item" style="left:73px"><time>Sep29, 2014</time><p>Aliquam molestie, mi et imperdiet euismod, dui purus auctor tellus, et interdum lacus lectus et ante. Sed accumsan sollicitudin sapien, sit amet adipiscing turpis gravida ac.</p><a href="#">Read More ››</a></article>
  <div class="news-divider" style="left:405px"></div>
  <article class="news-item" style="left:434px"><time>Sep29, 2014</time><p>Aliquam molestie, mi et imperdiet euismod, dui purus auctor tellus, et interdum lacus lectus et ante. Sed accumsan sollicitudin sapien, sit amet adipiscing turpis gravida ac.</p><a href="#">Read More ››</a></article>
  <div class="news-divider" style="left:766px"></div>
  <article class="news-item" style="left:794px"><time>Sep29, 2014</time><p>Aliquam molestie, mi et imperdiet euismod, dui purus auctor tellus, et interdum lacus lectus et ante. Sed accumsan sollicitudin sapien, sit amet adipiscing turpis gravida ac.</p><a href="#">Read More ››</a></article>
  <a class="btn" href="#">READ ALL NEWS ››</a>
</section>

<section class="clients">
  <h2 class="section-title">CLIENTS</h2>
  <div class="client-row">
    <span>Fernmarket</span><span>Quorvex</span><span>Linkwell</span><span>Tallow</span><span>Kirevo</span><span>Brenlo</span><span>Maxiform</span><span>Adrel</span><span>Civano</span>
  </div>
</section>

<section class="team">
  <h2 class="section-title">OUR TEAM</h2>
  <div class="member" style="left:73px">
    <div class="member-photo" role="img" aria-label="Portrait photo of a team member"></div>
    <div class="member-body"><h4>Name Heading</h4><p>Aliquam molestie, mi et imperdiet euismod, dui purus auctor tellus, et interdum lacus lectus et ante. Sed accumsan sollicitudin sapien, sit amet adipiscing turpis gravida ac.</p><a href="#">Read More About ››</a></div>
  </div>
  <div class="member" style="left:614px">
    <div class="member-photo" role="img" aria-label="Portrait photo of a team member"></div>
    <div class="member-body"><h4>Name Heading</h4><p>Aliquam molestie, mi et imperdiet euismod, dui purus auctor tellus, et interdum lacus lectus et ante. Sed accumsan sollicitudin sapien, sit amet adipiscing turpis gravida ac.</p><a href="#">Read More About ››</a></div>
  </div>
</section>

<footer class="site-footer">
  <h2 class="section-title">CONTACT US</h2>
  <div class="footer-col" style="left:73px">
    <h5>CONTACT ADDRESS</h5>
    <p class="address">Flat 12 Marlow House<br>48 Kestrel Row<br>London , Greater London<br>SW9 4QT</p>
    <p class="address" style="margin-top:4px">Ph: <strong>123-456-7890</strong></p>
    <p class="address" style="margin-top:4px">Email: <strong>info@companyname.com</strong></p>
  </div>
  <div class="footer-col" style="left:306px"><h5>OUR LOCATION</h5></div>
  <div class="map" role="img" aria-label="Street map of south-west London with the office location marked">
    <div class="map-popup">Pellwick Ltd in London, United Kingdom - 05927318<br>Flat 12 Marlow House<br>48 Kestrel Row<br>London, SW9 4QT</div>
    <svg class="map-pin" width="16" height="24" viewBox="0 0 16 24"><path d="M8 0a8 8 0 0 1 8 8c0 6-8 16-8 16S0 14 0 8a8 8 0 0 1 8-8z" fill="#d9372b"/><circle cx="8" cy="8" r="3" fill="#8e1c14"/></svg>
  </div>
  <div class="footer-col" style="left:884px">
    <h5>CONNECT US</h5>
    <div class="social"><span aria-label="Social link 1"></span><span aria-label="Social link 2"></span><span aria-label="Social link 3"></span><span aria-label="Feed link"></span></div>
  </div>
  <div class="footer-brand"><span class="brand-mark"></span>Pellwick</div>
  <p class="legal">Copyright ©2014, All Right Reserved<br>Privacy Policy</p>
</footer>

</body>
</html>
```